North Carolina-themed postcard

Would like 3x distinct designs for a postcard (sized 4.5 x 5.5) that celebrates the state of North Carolina. A vintage theme, a modern theme, and a simple black/white theme would be suggestions for design styles.

```html
<!DOCTYPE html>
<html lang="en">
<head>
<meta charset="utf-8">
<title>Greetings from North Carolina – Postcard</title>
<link rel="stylesheet" href="https://fonts.googleapis.com/css2?family=Chango&family=Courgette&family=Open+Sans:wght@600&display=swap">
<style>
  :root {
    --card-dark: #2f2f31;
    --card-ray: #3b3b3d;
    --gold-deep: #b5661f;
    --gold-mid: #e0a346;
    --gold-light: #f7e3a3;
    --gold-cream: #fff3cf;
    --script-yellow: #f2d21a;
    --caption-white: #ffffff;
    --cardinal-red: #6e1a14;
    --dogwood-blue: #6d7c99;
  }
  html, body {
    margin: 0;
    width: 1200px;
    height: 696px;
    overflow: hidden;
    background: #d6d6d6;
  }
  .postcard {
    position: relative;
    width: 1200px;
    height: 696px;
    background:
      repeating-conic-gradient(from 0deg at 50% 52%, var(--card-ray) 0deg 7deg, var(--card-dark) 7deg 15deg);
    overflow: hidden;
  }
  .postcard__frame {
    position: absolute;
    inset: 0;
  }
  .ornament {
    position: absolute;
    border-radius: 50%;
    background: radial-gradient(circle, var(--gold-cream) 0%, var(--gold-mid) 45%, var(--gold-deep) 75%, transparent 76%);
    opacity: 0.9;
  }
  .ornament--top-centre { left: 440px; top: 34px; width: 220px; height: 120px; border-radius: 0 0 50% 50%; }
  .ornament--bottom-centre { left: 600px; top: 540px; width: 230px; height: 125px; border-radius: 50% 50% 0 0; }
  .ornament--medallion { width: 74px; height: 74px; }
  .ornament--left-1 { left: 62px; top: 200px; }
  .ornament--left-2 { left: 62px; top: 330px; }
  .ornament--left-3 { left: 62px; top: 460px; }
  .ornament--right-1 { left: 1070px; top: 80px; }
  .ornament--right-2 { left: 1070px; top: 200px; }
  .ornament--right-3 { left: 1070px; top: 320px; }

  .state-emblems {
    position: absolute;
    left: 830px;
    top: 66px;
    width: 210px;
    height: 130px;
    border-radius: 40% 50% 45% 50%;
    background: linear-gradient(120deg, var(--dogwood-blue) 0%, #4a4d5a 40%, var(--cardinal-red) 70%, #4a1510 100%);
    opacity: 0.85;
  }
  .greeting {
    position: absolute;
    left: 140px;
    top: 160px;
    margin: 0;
    font-family: "Courgette", cursive;
    font-size: 50px;
    line-height: 0.95;
    color: var(--script-yellow);
    transform: rotate(-16deg);
    text-shadow: 0 2px 0 #7a5a00;
  }
  .greeting__line { display: block; }
  .greeting__line--from { padding-left: 58px; }
  .state-name {
    position: absolute;
    left: 190px;
    top: 282px;
    margin: 0;
    font-family: "Chango", sans-serif;
    font-weight: 400;
    font-size: 88px;
    line-height: 1.05;
    letter-spacing: 2px;
    white-space: nowrap;
    background: linear-gradient(100deg, var(--gold-deep) 0%, var(--gold-mid) 35%, var(--gold-cream) 55%, var(--gold-mid) 75%, var(--gold-light) 100%);
    -webkit-background-clip: text;
    background-clip: text;
    color: transparent;
  }
  .state-name__line { display: block; }
  .state-name__line--second { padding-left: 130px; }
  .landmark {
    position: absolute;
    left: 925px;
    top: 470px;
    width: 195px;
    margin: 0;
  }
  .landmark__caption {
    margin: 0 0 6px;
    font-family: "Open Sans", sans-serif;
    font-weight: 600;
    font-size: 14px;
    color: var(--caption-white);
    text-align: center;
  }
  .landmark__photo {
    height: 110px;
    border-radius: 14px;
    background: radial-gradient(ellipse at 50% 55%, #e0c47a 0%, #a98a45 35%, #3f5a88 75%, #2a3d66 100%);
  }
</style>
</head>
<body>
  <main class="postcard">
    <svg class="postcard__frame" width="1200" height="696" viewBox="0 0 1200 696" aria-hidden="true">
      <defs>
        <linearGradient id="gold-line" x1="0" y1="0" x2="1" y2="1">
          <stop offset="0" stop-color="#b5661f"/>
          <stop offset="0.35" stop-color="#f7e3a3"/>
          <stop offset="0.65" stop-color="#e0a346"/>
          <stop offset="1" stop-color="#b5661f"/>
        </linearGradient>
      </defs>
      <rect x="36" y="36" width="1128" height="624" rx="38" fill="none" stroke="url(#gold-line)" stroke-width="8"/>
      <rect x="52" y="52" width="1096" height="592" rx="30" fill="none" stroke="url(#gold-line)" stroke-width="2"/>
      <path d="M36 110 Q36 36 110 36" fill="none" stroke="url(#gold-line)" stroke-width="14" stroke-linecap="round"/>
      <path d="M1090 36 Q1164 36 1164 110" fill="none" stroke="url(#gold-line)" stroke-width="14" stroke-linecap="round"/>
      <path d="M36 586 Q36 660 110 660" fill="none" stroke="url(#gold-line)" stroke-width="14" stroke-linecap="round"/>
      <path d="M1090 660 Q1164 660 1164 586" fill="none" stroke="url(#gold-line)" stroke-width="14" stroke-linecap="round"/>
    </svg>

    <div class="ornament ornament--top-centre" role="img" aria-label="Gold filigree scroll ornament"></div>
    <div class="ornament ornament--bottom-centre" role="img" aria-label="Gold filigree scroll ornament"></div>
    <div class="ornament ornament--medallion ornament--left-1" role="img" aria-label="Gold lace medallion"></div>
    <div class="ornament ornament--medallion ornament--left-2" role="img" aria-label="Gold lace medallion"></div>
    <div class="ornament ornament--medallion ornament--left-3" role="img" aria-label="Gold lace medallion"></div>
    <div class="ornament ornament--medallion ornament--right-1" role="img" aria-label="Gold lace medallion"></div>
    <div class="ornament ornament--medallion ornament--right-2" role="img" aria-label="Gold lace medallion"></div>
    <div class="ornament ornament--medallion ornament--right-3" role="img" aria-label="Gold lace medallion"></div>

    <div class="state-emblems" role="img" aria-label="Cardinal in flight beside dogwood blossoms"></div>

    <p class="greeting">
      <span class="greeting__line">Greetings</span>
      <span class="greeting__line greeting__line--from">from</span>
    </p>

    <h1 class="state-name">
      <span class="state-name__line">NORTH</span>
      <span class="state-name__line state-name__line--second">CAROLINA</span>
    </h1>

    <figure class="landmark">
      <figcaption class="landmark__caption">State Capitol In Raleigh</figcaption>
      <div class="landmark__photo" role="img" aria-label="Photograph of the State Capitol building in Raleigh at dusk"></div>
    </figure>
  </main>
</body>
</html>
```